Redesign Video/PIcture Check in Page

Redesign our current TallyPointApp iPhone App checkin screens - Keep the design simple so that programmers do not have to do too much extra work to make your design work. - Look at the attached website screenshot for the overall look and feel, and color scheme - Convert the attached vector logo to iOS Icon format. - Deliver all graphics in the density required for iPhone XS Max. I will upload current check in pages that need to be reimagined. Check in needs to be more intutitive. Would like to add some gamification to the verification screen where they currently are required to enter series of random numbers. simple card game etc might work better. See TallyPointapp in itunes and google play store. also visit vormlink.example or tallypointapp.example for more information about our company.
The Current Checkin Process:
A. Client receives alert to checkin or submits voluntary checkin
B. Clicks checkin button on home Screen.
Redesign from here:
C. Clicks on a check in from check in list screen(new screen)
D. Enters verification number(gamification something better than random numbers)
E. Opens Camera
D. Takes Selfie
F. submits photo
G. clicks check in
SEE CURRENT STEPS PIC I UPLOADED

Target Market(s)

Courts,Probation and parole,Attorneys,Sheriffs,Jails, Alternative sentencing

Colors
3277b5

Requirements
Must have
• Must be easy to navigate,Intuitive!
Nice to have
• Gamification of check in verification.
• Step by step process with next button or similar

```html
<!DOCTYPE html>
<html lang="en">
<head>
<meta charset="utf-8">
<title>Check-in</title>
<link rel="stylesheet" href="https://fonts.googleapis.com/css2?family=Montserrat:wght@400;500;600;700;800&family=Open+Sans:wght@400&display=swap">
<style>
  :root {
    --brand-top: #3277b5;
    --brand-mid: #3663ad;
    --brand-bottom: #3d4ca2;
    --ring-1: #3a58a8;
    --ring-2: #3651a2;
    --ring-3: #334a9b;
    --ring-4: #304495;
    --ring-5: #2d3d8e;
    --photo-tone: #4a4a5a;
    --text: #ffffff;
    --text-faded: rgba(255, 255, 255, 0.42);
    --field: #ffffff;
    --plus-ring: #aab3d8;
    --plus-icon: #3a5fae;
  }
  * { margin: 0; padding: 0; box-sizing: border-box; }
  html, body { width: 675px; height: 1200px; overflow: hidden; }
  body {
    position: relative;
    font-family: "Montserrat", sans-serif;
    color: var(--text);
    background: linear-gradient(180deg, var(--brand-top) 0%, var(--brand-mid) 50%, var(--brand-bottom) 100%);
  }
  .abs { position: absolute; white-space: nowrap; }

  .status-bar { top: 14px; left: 0; width: 675px; height: 26px; font-size: 20px; font-weight: 500; }
  .status-carrier { left: 20px; top: 0; display: flex; align-items: center; gap: 8px; }
  .status-right { right: 20px; top: 0; display: flex; align-items: center; gap: 8px; }

  .nav-bar { top: 70px; left: 0; width: 675px; height: 32px; }
  .nav-title { left: 0; width: 675px; text-align: center; top: 2px; font-size: 20px; font-weight: 600; letter-spacing: 0.2px; }
  .nav-menu { left: 22px; top: 4px; }
  .nav-next { left: 638px; top: 5px; }

  .request-date { left: 35px; top: 171px; font-family: "Open Sans", sans-serif; font-size: 14.5px; color: var(--text-faded); }
  .request-title { left: 36px; top: 199px; font-size: 20px; font-weight: 400; }
  .request-hint { left: 35px; top: 234px; font-size: 14px; font-weight: 500; }
  .request-code { left: 33px; top: 271px; font-weight: 800; font-size: 43px; letter-spacing: -0.5px; line-height: 1.2; }

  .field { background: var(--field); border-radius: 14px; height: 72px; }
  .field-code { left: 36px; top: 348px; width: 603px; }
  .field-label { left: 36px; top: 455px; font-size: 19.5px; font-weight: 400; }
  .field-comment { left: 40px; top: 500px; width: 603px; }

  .rings { left: 124px; top: 594px; }
  .selfie {
    left: 255px; top: 726px; width: 164px; height: 164px; border-radius: 50%;
    background: radial-gradient(circle at 50% 40%, #6a6470 0%, var(--photo-tone) 55%, #1f2a55 100%);
  }
  .checkin-button { left: 302px; top: 949px; }
  .checkin-label { left: 0; width: 675px; text-align: center; top: 1032px; font-size: 18px; font-weight: 600; }

  .tab-bar { left: 0; top: 1100px; width: 675px; height: 100px; }
  .tab { top: 12px; width: 130px; margin-left: -65px; text-align: center; font-size: 17px; font-weight: 500; }
  .tab svg { display: block; margin: 0 auto 9px; height: 26px; }
  .tab-home { left: 62px; }
  .tab-checkins { left: 205px; }
  .tab-map { left: 448px; }
  .tab-howto { left: 610px; }
  .tab-add { left: 303px; top: 9px; }
</style>
</head>
<body>

  <div class="abs status-bar">
    <div class="abs status-carrier">
      <svg width="62" height="12" viewBox="0 0 62 12" fill="#fff">
        <circle cx="6" cy="6" r="5"/><circle cx="18" cy="6" r="5"/><circle cx="30" cy="6" r="5"/><circle cx="42" cy="6" r="5"/>
        <circle cx="54" cy="6" r="4.3" fill="none" stroke="#fff" stroke-width="1.3"/>
      </svg>
      <span>Carrier</span>
      <svg width="20" height="15" viewBox="0 0 20 15" fill="none" stroke="#fff" stroke-width="2.2" stroke-linecap="round">
        <path d="M2 5.5a11.5 11.5 0 0 1 16 0"/><path d="M5 8.7a7 7 0 0 1 10 0"/><circle cx="10" cy="12.5" r="1.5" fill="#fff" stroke="none"/>
      </svg>
    </div>
    <div class="abs status-right">
      <svg width="18" height="18" viewBox="0 0 18 18" fill="none" stroke="#fff" stroke-width="1.5">
        <path d="M15.5 9a6.5 6.5 0 1 1-2-4.7"/><path d="M13.5 1.8v2.7h-2.7"/>
        <rect x="6" y="8" width="6" height="4.5" rx="0.8" fill="#fff" stroke="none"/><path d="M7.2 8V6.8a1.8 1.8 0 0 1 3.6 0V8" stroke-width="1.2"/>
      </svg>
      <span>100%</span>
      <svg width="44" height="20" viewBox="0 0 44 20">
        <rect x="1" y="2" width="38" height="16" rx="3.5" fill="none" stroke="#fff" stroke-width="1.5"/>
        <rect x="3.5" y="4.5" width="33" height="11" rx="2" fill="#fff"/>
        <path d="M41 7.5v5a2.5 2.5 0 0 0 0-5z" fill="#fff"/>
      </svg>
    </div>
  </div>

  <header class="abs nav-bar">
    <svg class="abs nav-menu" width="31" height="22" viewBox="0 0 31 22" fill="#fff">
      <rect x="0" y="0" width="4" height="4"/><rect x="7" y="0.5" width="24" height="3"/>
      <rect x="0" y="9" width="4" height="4"/><rect x="7" y="9.5" width="24" height="3"/>
      <rect x="0" y="18" width="4" height="4"/><rect x="7" y="18.5" width="24" height="3"/>
    </svg>
    <h1 class="abs nav-title">CHECK-IN</h1>
    <svg class="abs nav-next" width="16" height="24" viewBox="0 0 16 24" fill="none" stroke="#fff" stroke-width="3.4" stroke-linecap="round" stroke-linejoin="round">
      <path d="M3 3l9 9-9 9"/>
    </svg>
  </header>

  <p class="abs request-date">20 Nov 2018 10 : 47 : 59</p>
  <h2 class="abs request-title">Voluntary Check-in Request</h2>
  <p class="abs request-hint">please check-in and Quote this Number:</p>
  <p class="abs request-code">9BKU</p>

  <div class="abs field field-code"></div>
  <p class="abs field-label">Comment</p>
  <div class="abs field field-comment"></div>

  <svg class="abs rings" width="427" height="427" viewBox="0 0 427 427">
    <circle cx="213.5" cy="213.5" r="213" fill="var(--ring-1)" opacity="0.8"/>
    <circle cx="213.5" cy="213.5" r="184" fill="var(--ring-2)"/>
    <circle cx="213.5" cy="213.5" r="154" fill="var(--ring-3)"/>
    <circle cx="213.5" cy="213.5" r="125" fill="var(--ring-4)"/>
    <circle cx="213.5" cy="213.5" r="102" fill="var(--ring-5)"/>
  </svg>
  <div class="abs selfie" role="img" aria-label="Client selfie photo"></div>

  <svg class="abs checkin-button" width="70" height="70" viewBox="0 0 70 70" fill="none" stroke="#fff" stroke-width="5" stroke-linecap="round" stroke-linejoin="round">
    <path d="M58 27a29 29 0 1 1-12-17"/>
    <path d="M22 33l12 12 30-32"/>
  </svg>
  <p class="abs checkin-label">Check-in</p>

  <nav class="abs tab-bar">
    <div class="abs tab tab-home">
      <svg width="28" height="24" viewBox="0 0 28 24" fill="#fff"><path d="M14 1L1 12.5h4V23h7v-7h4v7h7V12.5h4z"/></svg>
      Home
    </div>
    <div class="abs tab tab-checkins">
      <svg width="30" height="24" viewBox="0 0 30 24" fill="none" stroke="#fff" stroke-width="5" stroke-linecap="round" stroke-linejoin="round"><path d="M4 13l7 7L26 4"/></svg>
      Check-ins
    </div>
    <svg class="abs tab-add" width="74" height="74" viewBox="0 0 74 74">
      <circle cx="37" cy="37" r="35" fill="#fff" stroke="var(--plus-ring)" stroke-width="4"/>
      <path d="M37 25v24M25 37h24" stroke="var(--plus-icon)" stroke-width="3" stroke-linecap="round"/>
    </svg>
    <div class="abs tab tab-map">
      <svg width="20" height="26" viewBox="0 0 20 26" fill="#fff"><path d="M10 0a9 9 0 0 0-9 9c0 7 9 17 9 17s9-10 9-17a9 9 0 0 0-9-9zm0 12.5a3.5 3.5 0 1 1 0-7 3.5 3.5 0 0 1 0 7z"/></svg>
      Map
    </div>
    <div class="abs tab tab-howto">
      <svg width="16" height="28" viewBox="0 0 16 28" fill="#fff"><circle cx="10" cy="3.5" r="3.2"/><path d="M5 10h7l-3.5 13H12l-.8 3H3l3.4-13H4z"/></svg>
      How To
    </div>
  </nav>

</body>
</html>
```